Webdesign für freiberuflichen Statiker
Zielgruppe
Ich bin seit 2021 freiberuflicher Statiker. Ich arbeite mit anderen Freelancern / Partnern / Firmen zusammen und lasse von ihnen z.B. Pläne zeichnen. Meine aktuelle Website habe ich selbst designed, mit Wordpress. Diese soll nun aber komplett neu gestaltet werden. Meine Domain www.vendrik-statik.de möchte ich möglichst behalten.
Meine Zielgruppe sind Architekturbüros, Bauträger, private und öffentliche Bauherren. Sie sollen vor allem einen visuellen Eindruck von unserer Arbeit bekommen - durch Fotos (und einem Video auf der Startseite) von Baustellen, von unseren 3D-Modellen oder Berechnungsmodellen.
Aufgabenstellung
Es gibt bereits ein neues Logo. Dieses werde ich mit anhängen. Außerdem habe ich eine pdf-Datei vorbereitet ('SBV_Inhalte Website'), die den groben Aufbau der Website vorgibt und der die Texte entnommen werden können. Auf der ersten Seite des Dokuments stehen außerdem 3 Beispiel-Websites, die ich gut finde und an denen Ihr euch orientieren könnt. Die Farbwahl kann sehr schlicht gehalten werden - ähnlich wie bei den 3 Beispiel-Seiten. Ich liefere eigene Bilder mit, für projektunabhängige Inhalte können aber auch andere Bilder verwendet werden.

```html
<!DOCTYPE html>
<html lang="de">
<head>
<meta charset="utf-8">
<title>Neubau Hotel Merkur – SBV</title>
<link href="https://fonts.googleapis.com/css2?family=Montserrat:wght@400;500;600&display=swap" rel="stylesheet">
<style>
  :root {
    --ink: #111111;
    --text: #3a3a3a;
    --accent: #e07a72;
    --line: #9a9a9a;
    --paper: #ffffff;
    --footer: #000000;
  }
  * { margin: 0; padding: 0; box-sizing: border-box; }
  html, body { width: 769px; height: 1200px; overflow: hidden; }
  body { position: relative; background: var(--paper); color: var(--ink); font-family: "Montserrat", sans-serif; }
  .abs { position: absolute; }
  .rule { position: absolute; height: 1px; background: var(--accent); }

  .brand { left: 79px; top: 14px; font-size: 22px; font-weight: 500; line-height: 26px; letter-spacing: 1px; }
  .menu { left: 666px; top: 22px; width: 23px; height: 16px; }
  .menu span { display: block; height: 1.3px; background: var(--ink); margin-bottom: 6px; }

  .hero-photo { left: 445px; top: 0; width: 324px; height: 279px;
    background: linear-gradient(160deg, #cfd2d4 0%, #e4e4e2 40%, #d9d6d2 70%, #cbc4bb 100%); }
  .hero-divider { left: 0; top: 279px; width: 769px; height: 1px; background: var(--line); }
  .eyebrow { left: 131px; top: 82px; font-size: 12px; font-weight: 500; }
  .title { left: 79px; top: 120px; font-size: 40px; font-weight: 500; line-height: 42px; letter-spacing: 0.3px; }
  .meta { top: 238px; font-size: 12px; display: flex; align-items: center; gap: 5px; }
  .meta svg { width: 12px; height: 12px; }

  .details { left: 79px; top: 341px; width: 245px; height: 283px; border: 1px solid var(--line); }
  .details h3 { text-align: center; font-size: 11.5px; font-weight: 500; margin-top: 12px; }
  .details dl { position: absolute; left: 12px; top: 45px; width: 225px; font-size: 10px; }
  .detail-row { display: flex; min-height: 24.5px; }
  .detail-row dt { width: 104px; font-weight: 400; color: var(--text); }
  .detail-row dd { flex: 1; font-weight: 500; line-height: 16px; }
  .detail-row.tall { min-height: 40px; }

  .section-head { font-size: 23px; font-weight: 500; letter-spacing: 0.2px; }
  .description { left: 341px; width: 340px; }
  .description p { font-size: 10px; line-height: 15.8px; color: var(--text); margin-bottom: 15.8px; }

  .nav-btn { top: 689px; width: 35px; height: 35px; border: 1px solid var(--ink); display: flex; align-items: center; justify-content: center; }
  .nav-btn svg { width: 22px; height: 14px; }
  .gallery-photo { top: 737px; width: 192px; height: 98px;
    background: linear-gradient(170deg, #7e8584 0%, #c9c8c5 45%, #a9a29a 75%, #8b8173 100%); }

  .cta { left: 0; top: 897px; width: 769px; height: 203px;
    background: linear-gradient(120deg, #efe6da 0%, #f7f2ea 35%, #e8dccb 65%, #f4efe8 100%); }
  .cta-head { left: 79px; top: 977px; font-size: 23px; font-weight: 500; line-height: 27px; }
  .cta-btn { left: 498px; top: 977px; width: 192px; height: 34px; border: 1px solid var(--ink);
    display: flex; align-items: center; justify-content: center; gap: 8px; font-size: 12px; font-weight: 500; }

  .footer { left: 0; top: 1100px; width: 769px; height: 100px; background: var(--footer); color: #fff; }
  .footer .brand { top: 24px; left: 80px; color: #fff; }
  .footer-links { right: 79px; top: 45px; font-size: 9.5px; display: flex; gap: 9px; }
  .copyright { left: 80px; top: 76px; font-size: 8px; }
</style>
</head>
<body>
  <div class="abs brand">SBV</div>
  <div class="abs hero-photo" role="img" aria-label="Luftaufnahme des eingerüsteten Hotelrohbaus"></div>
  <div class="abs menu"><span></span><span></span><span></span></div>

  <div class="rule" style="left:79px;top:89px;width:35px"></div>
  <div class="abs eyebrow">BAUJAHR 20XX</div>
  <h1 class="abs title">NEUBAU HOTEL<br>MERKUR</h1>

  <div class="abs meta" style="left:76px">
    <svg viewBox="0 0 12 12" fill="none" stroke="#d9534f" stroke-width="0.9"><path d="M1 4l3-1.2 4 1.2 3-1.2v7.4l-3 1.2-4-1.2-3 1.2z"/><circle cx="7" cy="4.2" r="1.4"/></svg>
    VELBERT, DEUTSCHLAND
  </div>
  <div class="abs meta" style="left:285px">
    <svg viewBox="0 0 12 12" fill="none" stroke="#d9534f" stroke-width="1" stroke-dasharray="2 1.2"><rect x="1" y="1" width="10" height="10"/></svg>
    CA. 4600 QM
  </div>
  <div class="abs hero-divider"></div>

  <section class="abs details">
    <h3>PROJEKT DETAILS</h3>
    <dl>
      <div class="detail-row"><dt>Standort</dt><dd>Velbert, Deutschland</dd></div>
      <div class="detail-row"><dt>Jahr</dt><dd>20XX</dd></div>
      <div class="detail-row"><dt>Bauart</dt><dd>Massivbau</dd></div>
      <div class="detail-row"><dt>Baugrundfläche</dt><dd>ca. 4600 qm</dd></div>
      <div class="detail-row"><dt>Geschosse</dt><dd>7 Vollgeschosse</dd></div>
      <div class="detail-row"><dt>Leistung</dt><dd>LP 5</dd></div>
      <div class="detail-row"><dt>Bauherr</dt><dd>Hotel Wiesental GmbH</dd></div>
      <div class="detail-row tall"><dt>Architekt</dt><dd>Halvorsen Hotel Concepts</dd></div>
      <div class="detail-row"><dt>Auftrageber</dt><dd>Hotel Wiesental GmbH</dd></div>
    </dl>
  </section>

  <div class="rule" style="left:341px;top:340px;width:139px"></div>
  <h2 class="abs section-head" style="left:341px;top:352px">PROJEKTBESCHREIBUNG</h2>
  <div class="abs description" style="top:390px">
    <p>Lorem ipsum dolor sit amet, consetetur sadipscing elitr, sed diam nonumy eirmod tempor invidunt ut labore et dolore magna aliquyam erat, sed diam voluptua. At vero eos et accusam et justo duo dolores et ea rebum. Stet clita kasd gubergren, no sea takimata sanctus est Lorem ipsum dolor sit amet.</p>
    <p>Lorem ipsum dolor sit amet, consetetur sadipscing elitr, sed diam nonumy eirmod tempor invidunt ut labore et dolore magna aliquyam erat, sed diam voluptua. At vero eos et accusam et justo duo dolores et ea rebum. Stet clita kasd gubergren, no sea takimata sanctus est Lorem ipsum dolor sit amet.</p>
  </div>

  <div class="rule" style="left:79px;top:684px;width:140px"></div>
  <h2 class="abs section-head" style="left:79px;top:695px">PROJEKTGALERIE</h2>
  <div class="abs nav-btn" style="left:602px"><svg viewBox="0 0 22 14" fill="none" stroke="#111" stroke-width="1.3"><path d="M21 7H1M7 1L1 7l6 6"/></svg></div>
  <div class="abs nav-btn" style="left:655px"><svg viewBox="0 0 22 14" fill="none" stroke="#111" stroke-width="1.3"><path d="M1 7h20M15 1l6 6-6 6"/></svg></div>
  <div class="abs gallery-photo" style="left:79px" role="img" aria-label="Baustelle Hotel aus der Vogelperspektive"></div>
  <div class="abs gallery-photo" style="left:288px" role="img" aria-label="Rohbau mit Gerüst und Kreuzung"></div>
  <div class="abs gallery-photo" style="left:497px" role="img" aria-label="Hotelrohbau im Stadtbild"></div>

  <div class="abs cta" role="img" aria-label="Helle Holztragwerkskonstruktion von unten"></div>
  <div class="rule" style="left:79px;top:964px;width:140px"></div>
  <h2 class="abs cta-head">WIR SIND IHR ZUVERLÄSSIGER<br>PARTNER</h2>
  <a class="abs cta-btn">KONTAKT AUFNEHMEN
    <svg width="16" height="12" viewBox="0 0 16 12" fill="none" stroke="#111" stroke-width="1.2"><path d="M1 6h14M10 1l5 5-5 5"/></svg>
  </a>

  <footer class="abs footer">
    <div class="abs brand">SBV</div>
    <nav class="abs footer-links"><span>Impressum</span><span>Datenschutz</span></nav>
    <div class="abs copyright">© 2024 nordlicht-media.de</div>
  </footer>
</body>
</html>
```